WP website design (Whitlock)

We need a wordpress design for an established auction and real estate company based in Daswon Creek, Canada. The winning design will incorporate a professional color scheme with company logo in a clean layout with specified widgets. The design needs to consider that this will be developed on a responsive theme. Colors will complement logo - red, black and gray.

Industry/Entity Type

Real Estate

Font styles to use
Sans Serif

Requirements
Must have
• Must Have:
the main logo is provided and the 'horse' logo shouldbe incorporated into the hearder or sidebar (either left or right)as well. Contact info should be placed in the header, and footer too: (250) 555-0143
(250) 555-0178
(250) 555-0192
rvm@zorquil.bc.ca

- Navigation:
1) Home 2) Auctions 3) Online Auctions 4) About Us 5) Contact Us

Home Page will have following:
"Family owned and operated with a family guarantee.
Located in Dawson Creek, B.C. Canada

Competitive Rates Bonded & Licensed Livestock Dealers & Auctioneers
All Types of Auction Sales in B.C. & Alberta

Farm, Machinery
Equipment Sales
Household & Estate Sales
Livestock Marketing Consultants
Field Cattle Sales
Livestock Pedigree Sales
Horse Sales Appraisals"

Homepage will have auctions - as at http://brindlevexsales.com/upcoming-auctions/.

Footer will have smaller company logo, credit card logo, and attached association logos and this contact info:
.(620) 555-0117: OFFICE
(620) 555-0164: FAX
hgrup@vxq.com: email
Address: 718 N. Birch Ave., Johnson KS
Mailing Address: PO Box 839, Johnson, KS

Widgets:
1) email sign up 2) News blog widget 3) testimonial blog widget 4) featured auctions widget 5) the 'Gold Peg' logo which is included
Nice to have
• Nice to Have:
- demonstrate the drop-down menu styling, e.g. under Auctions
- Upcoming Auctions
- Past Auctions

```html
<!DOCTYPE html>
<html lang="en">
<head>
<meta charset="utf-8">
<title>Whitlock's Auction Mart Ltd.</title>
<link href="https://fonts.googleapis.com/css2?family=Arimo:wght@400;700&family=PT+Sans:wght@400;700&display=swap" rel="stylesheet">
<style>
:root{
  --red:#e5333a;
  --red-dark:#c8252c;
  --ink:#222;
  --dark:#2f2f2f;
  --dark-2:#474747;
  --page:#ececec;
  --panel:#f7f7f7;
  --line:#dcdcdc;
  --white:#fff;
}
*{margin:0;padding:0;box-sizing:border-box}
html,body{width:907px;height:1200px;overflow:hidden}
body{position:relative;background:var(--page);font-family:Arimo,Arial,sans-serif;color:var(--ink);font-size:9px}
.abs{position:absolute}
a{color:inherit;text-decoration:none}

/* header */
.brand{left:90px;top:16px;width:136px;text-align:center;font-family:"PT Sans",sans-serif;font-weight:700;font-size:14px;line-height:17px;color:var(--ink);letter-spacing:.3px;white-space:nowrap}
.brand small{display:block;font-size:13px}
.brand-mark{left:150px;top:64px;width:14px;height:14px;border-radius:50%;background:var(--ink)}
.contact-phone{left:478px;top:40px;display:flex;align-items:center;gap:7px;color:var(--red);font-size:13.5px}
.contact-mail{left:630px;top:73px;display:flex;align-items:center;gap:9px;color:var(--red);font-size:10px}

/* nav */
.nav{left:0;top:109px;width:907px;height:32px;background:linear-gradient(#4a4a4a,#262626);z-index:4}
.nav a{position:absolute;top:10px;color:var(--white);font-size:10.5px}
.nav .active{top:5px;left:148px;width:114px;height:30px;background:var(--red);border:1px solid #f06a6f;border-bottom:none;border-radius:3px 3px 0 0;padding:6px 0 0 16px}
.nav .active::after{content:"⌄";position:absolute;right:6px;top:3px;font-size:10px}
.dropdown{left:148px;top:141px;width:141px;height:95px;background:var(--red);border:1px solid #f06a6f;border-radius:0 0 4px 4px;padding-top:6px;z-index:5}
.dropdown a{display:block;height:20px;padding:4px 0 0 8px;color:var(--white);font-size:10px}
.dropdown a.current{background:var(--dark)}

/* main column */
.main{left:77px;top:141px;width:753px;height:961px;background:var(--white)}
.hero{left:82px;top:156px;width:522px;height:262px;border-radius:8px 0 0 8px;background:linear-gradient(180deg,#d9dde0 0%,#c9cccf 45%,#7d9a4f 62%,#5f8a33 100%)}
.signup{left:604px;top:156px;width:221px;height:262px;background:var(--red);border-radius:0 8px 8px 0}
.signup h2{position:absolute;left:26px;top:14px;color:var(--white);font-family:"PT Sans",sans-serif;font-weight:400;font-size:16px;letter-spacing:.3px}
.field{position:absolute;left:24px;width:186px;height:27px;background:#f0eeee;border-radius:4px;padding:8px 0 0 6px;font-size:10px;color:#333;letter-spacing:.3px}
.btn{position:absolute;left:25px;top:176px;width:93px;height:29px;background:linear-gradient(#3e3e3e,#1c1c1c);border-radius:5px;color:var(--white);font-family:"PT Sans",sans-serif;font-size:14.5px;padding:5px 0 0 10px;letter-spacing:.4px}

.section-title{left:96px;top:436px;font-family:"PT Sans",sans-serif;font-weight:400;font-size:16.5px;color:#333;letter-spacing:.4px}

/* auction card */
.card{left:93px;width:491px;height:279px;background:var(--white);border:1px solid var(--line);border-radius:8px 8px 0 0;box-shadow:0 1px 2px rgba(0,0,0,.12)}
.card-head{position:absolute;left:-1px;top:-1px;width:491px;height:31px;background:linear-gradient(#4b4b4b,#1f1f1f);border-radius:8px 8px 0 0;color:var(--white);font-family:"PT Sans",sans-serif;font-weight:700;font-size:12.5px;padding:7px 0 0 7px;letter-spacing:.3px}
.thumb{position:absolute;left:8px;top:54px;width:87px;height:70px;border:1px solid var(--line);border-radius:4px;background:var(--panel);padding:5px}
.thumb div{width:100%;height:100%;background:linear-gradient(180deg,#8cb1d8 0%,#d7c9a9 50%,#6f8f3e 100%)}
.box{position:absolute;left:100px;width:349px;border:1px solid var(--line);border-radius:4px;background:var(--panel);padding:7px 7px;font-size:9px;line-height:13.6px;letter-spacing:.2px}
.box .red{color:var(--red)}
.box b{font-weight:700}
.box u{color:var(--red);font-weight:700}
.links{position:absolute;left:8px;top:136px;width:87px;height:78px;border:1px solid var(--line);border-radius:4px;background:var(--panel)}
.links h3{height:25px;background:var(--red);margin:2px 2px 0;border-radius:3px 3px 0 0;color:var(--white);font-family:"PT Sans",sans-serif;font-size:13px;padding:4px 0 0 9px;letter-spacing:.4px}
.links p{display:flex;align-items:center;gap:5px;margin:6px 0 0 7px;font-weight:700;font-size:10px;color:#333}

/* sidebar widgets */
.widget{left:605px;width:220px;background:var(--panel);border:1px solid var(--line);border-radius:8px}
.widget-head{height:32px;background:var(--red);border-radius:8px 8px 0 0;margin:-1px -1px 0;color:var(--white);font-family:"PT Sans",sans-serif;font-size:16.5px;padding:5px 0 0 17px;letter-spacing:.4px}
.more{position:absolute;left:26px;color:var(--red);font-style:italic;font-size:8.5px}
.feat-link{position:absolute;left:16px;top:40px;color:var(--red);font-size:9.5px;text-decoration:underline}
.feat-date{position:absolute;left:18px;top:62px;font-weight:700;font-size:8.5px;line-height:11px}
.feat-addr{position:absolute;left:18px;top:96px;font-size:8.5px;line-height:11px}
.feat-photo{position:absolute;left:121px;top:61px;width:94px;height:60px;background:linear-gradient(135deg,#9fb7d1,#c8ccd0 55%,#6d7f62)}
.news li{list-style:none;position:relative;padding-left:27px;font-size:8.3px;line-height:15px;color:#333}
.news li::before{content:"";position:absolute;left:16px;top:5px;border:3px solid transparent;border-left:3px solid #333}
.quote{position:absolute;left:23px;top:44px;font-size:8.3px;line-height:15px;color:#333}
.sign{position:absolute;left:138px;top:101px;font-style:italic;font-size:8.5px}
.partner{position:absolute;left:40px;top:24px;width:145px;height:72px;border:2px solid var(--ink);background:var(--white);display:flex;align-items:center;justify-content:center;gap:6px;font-family:"PT Sans",sans-serif;font-weight:700;font-size:17px;color:var(--red)}
.partner i{width:12px;height:12px;background:var(--red)}

/* footer */
.footer{left:0;top:1102px;width:907px;height:98px;background:#3c3c3c;color:var(--white);font-size:8.5px}
.footer p{position:absolute}
.cards{left:608px;top:56px;display:flex;gap:3px}
.cards span{width:28px;height:18px;border-radius:2px;background:#e9e9e9;border:1px solid #bbb}
.foot-brand{left:726px;top:20px;width:100px;text-align:center;font-family:"PT Sans",sans-serif;font-weight:700;font-size:9px;line-height:12px;color:var(--white);white-space:nowrap}
.foot-mark{left:770px;top:50px;width:10px;height:10px;border-radius:50%;background:var(--white)}
</style>
</head>
<body>

<div class="abs brand">WHITLOCK'S AUCTION<small>MART LTD.</small></div>
<div class="abs brand-mark"></div>

<div class="abs contact-phone">
  <svg width="19" height="19" viewBox="0 0 20 20"><circle cx="10" cy="10" r="9" fill="none" stroke="#111" stroke-width="1.6"/><path d="M6.5 5.5c.6-.6 1.3-.4 1.6.1l1 1.6c.3.5.1 1-.3 1.3l-.6.5c.5 1.2 1.5 2.2 2.7 2.7l.5-.6c.3-.4.8-.6 1.3-.3l1.6 1c.5.3.7 1 .1 1.6-2.7 2.6-10.5-5.2-7.9-7.9z" fill="#111"/></svg>
  <span>(250) 555-0143,&nbsp; 555-0178,&nbsp; 555-0192</span>
</div>
<div class="abs contact-mail">
  <svg width="17" height="12" viewBox="0 0 17 12"><rect x=".7" y=".7" width="15.6" height="10.6" fill="none" stroke="#111" stroke-width="1.2"/><path d="M.7.7l7.8 6 7.8-6M.7 11.3l6-5M16.3 11.3l-6-5" fill="none" stroke="#111" stroke-width="1.1"/></svg>
  <span>rvm@zorquil.bc.ca</span>
</div>

<nav class="abs nav">
  <a style="left:97px" href="#">Home</a>
  <a class="active" href="#">Auctions</a>
  <a style="left:308px" href="#">Online Auctions</a>
  <a style="left:418px" href="#">About Us</a>
  <a style="left:518px" href="#">Contact Us</a>
</nav>

<div class="abs main"></div>

<div class="abs hero" role="img" aria-label="Photo of a red farm tractor parked on grass in front of a barn"></div>

<div class="abs dropdown">
  <a href="#">Upcoming Auctions #1</a>
  <a class="current" href="#">Upcoming Auctions #2</a>
  <a href="#">Upcoming Auctions #3</a>
  <a href="#">Upcoming Auctions #4</a>
</div>

<form class="abs signup">
  <h2>EMAIL SIGN-UP FORM</h2>
  <div class="field" style="top:50px">First Name</div>
  <div class="field" style="top:90px">Last Name</div>
  <div class="field" style="top:134px">Email Address</div>
  <div class="btn">Subscribe</div>
</form>

<h1 class="abs section-title">Upcoming Auctions</h1>

<article class="abs card" style="top:471px">
  <div class="card-head">160± ACRES LAND TARROW COUNTY, OK</div>
  <div class="thumb"><div role="img" aria-label="House with a for sale sign"></div></div>
  <div class="box" style="top:56px">BILLINGS AREA * CROP &amp; TIMBER<br>
    <b class="red">160± ACRES LAND TARROW COUNTY</b><b>, OK ~ BILLINGS AREA * CROP &amp; TIMBER ~ EXCELLENT HUNTING</b><br>
    ABSOLUTE AUCTION<br>SELLER: THE MERIDIAN HERITAGE TRUST</div>
  <div class="links"><h3>LINKS</h3>
    <p><svg width="17" height="8"><rect width="6" height="7" fill="#222"/><path d="M8 1h9M8 4h9M8 7h9" stroke="#222" stroke-width="1.4"/></svg>Details</p>
    <p><svg width="16" height="14"><rect x="1" y="1" width="10" height="9" fill="none" stroke="#222" stroke-width="1.5"/><rect x="6" y="5" width="9" height="8" fill="#222"/></svg>Photos</p>
  </div>
  <div class="box" style="top:150px"><b>LIVE ON-SITE AUCTION WITH ONLINE BIDDING</b><br>
    Begins:&nbsp; Tuesday, March 12, 2013 at 10:00 AM CDT<br>
    <u>Click Here to Bid Online Now!</u><br>
    <b>Location:</b>&nbsp; See Directions<br>United States Harlow, OK 74699</div>
</article>

<article class="abs card" style="top:769px">
  <div class="card-head">160± ACRES LAND TARROW COUNTY, OK</div>
  <div class="thumb"><div role="img" aria-label="House with a for sale sign"></div></div>
  <div class="box" style="top:56px">BILLINGS AREA * CROP &amp; TIMBER<br>
    <b class="red">160± ACRES LAND TARROW COUNTY</b><b>, OK ~ BILLINGS AREA * CROP &amp; TIMBER ~ EXCELLENT HUNTING</b><br>
    ABSOLUTE AUCTION<br>SELLER: THE MERIDIAN HERITAGE TRUST</div>
  <div class="links"><h3>LINKS</h3>
    <p><svg width="17" height="8"><rect width="6" height="7" fill="#222"/><path d="M8 1h9M8 4h9M8 7h9" stroke="#222" stroke-width="1.4"/></svg>Details</p>
    <p><svg width="16" height="14"><rect x="1" y="1" width="10" height="9" fill="none" stroke="#222" stroke-width="1.5"/><rect x="6" y="5" width="9" height="8" fill="#222"/></svg>Photos</p>
  </div>
  <div class="box" style="top:150px"><b>LIVE ON-SITE AUCTION WITH ONLINE BIDDING</b><br>
    Begins:&nbsp; Tuesday, March 12, 2013 at 10:00 AM CDT<br>
    <u>Click Here to Bid Online Now!</u><br>
    <b>Location:</b>&nbsp; See Directions<br>United States Harlow, OK 74699</div>
</article>

<aside class="abs widget" style="top:441px;height:151px">
  <div class="widget-head">Featured Auctions</div>
  <a class="feat-link" href="#">TRACTOR * HI LIFT * MACHINERY</a>
  <p class="feat-date">Saturday March 16,<br>2013 at 10:00 AM EDT</p>
  <p class="feat-addr">Alder Road<br>Fenwick, KY 40099</p>
  <div class="feat-photo" role="img" aria-label="Photo of a silver minivan"></div>
  <a class="more" style="top:128px;left:22px" href="#">read more</a>
</aside>

<aside class="abs widget news" style="top:601px;height:149px">
  <div class="widget-head">News blog</div>
  <ul style="margin-top:14px">
    <li>Great Land Auction Companies Make<br>All the Difference Great Land Auction</li>
    <li style="margin-top:3px">Great Land Auction Companies Make</li>
  </ul>
  <a class="more" style="top:124px" href="#">read more</a>
</aside>

<aside class="abs widget" style="top:762px;height:156px">
  <div class="widget-head">Clients Testimonials</div>
  <p class="quote">Great Land Auction Companies Make<br>All the Difference Great Land Auction<br>Great Land Auction Companies Make</p>
  <p class="sign">Marguerite</p>
  <a class="more" style="top:125px" href="#">read more</a>
</aside>

<aside class="abs widget" style="top:930px;height:119px">
  <div class="partner"><i></i>Gold Peg</div>
</aside>

<footer class="abs footer">
  <p style="left:78px;top:26px">Copyright (C) Whitlocks. 2014.&nbsp; All Rights Reserved</p>
  <p style="left:79px;top:52px">Home -&nbsp; Auctions - Online Auctions - About us - Contact Us</p>
  <p style="left:79px;top:69px">Phone: .(620) 555-0117, Email: hgrup@vxq.com</p>
  <p style="left:360px;top:46px">Address: 718 N. Birch Ave., Johnson KS</p>
  <p style="left:360px;top:69px">Mailing Address: PO Box 839, Johnson, KS</p>
  <div class="abs cards"><span></span><span></span><span></span></div>
  <div class="abs foot-brand">WHITLOCK'S AUCTION<br>MART LTD.</div>
  <div class="abs foot-mark"></div>
</footer>

</body>
</html>
```